Australian Export Wine Label

Brand

To design a label based around Australia’s famous bush ranger Tom Brody called Brody’s Hollow.

Imagery for the label could be an abstract image of Tom’s armour of even of himself or we are open to other possibilities ranging from a traditional label to a more contemporary look and feel.

Images should not include guns and imagery used must be free of copyright.

Designs should be able to be printed by the standard 4 colour print process. As this is not an expensive product there will be no expensive label fiunishes such as gold foil or embossing

The range

The range of wines will consist of a 2011 Shiraz, 2012 Sauvignon Blanc and 2011 Chardonnay.

Market

The primary market for these wines is Ireland with the price range being in the $10-15 bracket. The wines will be available in independent retail shops and restaurants

Front Label Mandatories

1. Front Label: should not exceed 110mm x 80mm

2. Brand name - Brody’s Hollow

3. Vintage & Variety – for example 2011 Shiraz

4. Origin – Wine of Australia

5. Text to appear on front label: Born in Co. Antrim, the remarkable Martha Brody had eight children including Australia’s most famous Bushranger Tom Brody. The family’s wild and independent spirit is legendary in country Australia.

Back Label Mandatories

1. Back Label: 80mm x 80mm

2. Brand name

3. Vintage & Variety

4. Alcohol, Volume, Country of production

5. 13.0% VOL 750Ml (must be 4mm in height)

6. Contains egg, milk and nuts. Traces may remain

7. Please include the pregnant lady logo and a recycling logo

8. Wine of Australia

9. Space for barcode

10. Text to appear on back label (Shiraz):

Brody’s Hollow is our vineyard named after the Brody family, whose homestead stood here long before the vines were planted.
Our Brody’s Hollow Shiraz is bold and full of flavour. Plums, cassis, chocolate and spice intermingle on the nose and palate, resulting in a full bodied, vibrant wine. Enjoy with a spirit of adventure and a hearty beef stew.

```html
<!DOCTYPE html>
<html lang="en">
<head>
<meta charset="utf-8">
<title>Brody’s Hollow Shiraz – Front Label</title>
<link rel="stylesheet" href="https://fonts.googleapis.com/css2?family=Cedarville+Cursive&family=Josefin+Sans:wght@300;400;700&display=swap">
<style>
  :root {
    --backdrop: #5e5e5e;
    --label-paper: #ece8e4;
    --label-edge: #d9d4cf;
    --wine-red: #7a1f3d;
    --ink: #3a3536;
    --ink-soft: #5a5455;
    --art-dark: #4a4647;
    --art-light: #a9a4a3;
  }
  * { box-sizing: border-box; margin: 0; padding: 0; }
  html, body {
    width: 1200px;
    height: 837px;
    overflow: hidden;
  }
  body {
    background: radial-gradient(ellipse at 50% 40%, #6e6e6e 0%, var(--backdrop) 70%);
    display: flex;
    align-items: center;
    justify-content: center;
    font-family: "Josefin Sans", "Helvetica Neue", Arial, sans-serif;
  }
  .front-label {
    width: 440px;
    height: 780px;
    background: var(--label-paper);
    border: 1px solid var(--label-edge);
    display: flex;
    flex-direction: column;
    align-items: center;
    padding-top: 50px;
    color: var(--ink);
  }
  .armour-artwork {
    width: 170px;
    height: 370px;
    border-radius: 6px;
    background: linear-gradient(180deg, var(--art-light) 0%, var(--art-dark) 55%, var(--art-light) 100%);
    opacity: 0.85;
  }
  .brand-name {
    margin-top: 40px;
    font-family: "Cedarville Cursive", "Brush Script MT", cursive;
    font-weight: 400;
    font-size: 50px;
    line-height: 1;
    color: var(--wine-red);
    letter-spacing: 1px;
  }
  .variety {
    margin-top: 38px;
    font-weight: 700;
    font-size: 17px;
    letter-spacing: 2px;
    text-transform: uppercase;
  }
  .origin {
    margin-top: 6px;
    font-weight: 300;
    font-size: 17px;
    letter-spacing: 4px;
    text-transform: uppercase;
  }
  .vintage {
    margin-top: 6px;
    font-weight: 300;
    font-size: 17px;
    letter-spacing: 6px;
    color: var(--ink-soft);
  }
  .heritage-note {
    margin-top: 30px;
    width: 340px;
    text-align: center;
    font-weight: 300;
    font-size: 14.5px;
    line-height: 1.55;
    color: var(--ink-soft);
  }
</style>
</head>
<body>
  <main class="front-label">
    <div class="armour-artwork" role="img" aria-label="Engraved illustration of a bushranger’s iron armour"></div>
    <h1 class="brand-name">Brody’s Hollow</h1>
    <p class="variety">Shiraz</p>
    <p class="origin">Wine of Australia</p>
    <p class="vintage">2011</p>
    <p class="heritage-note">Born in Co. Antrim, the remarkable Martha Brody had eight children including Australia’s most famous Bushranger Tom Brody. The family’s wild and independent spirit is legendary in country Australia.</p>
  </main>
</body>
</html>
```